Building Company Business Card Design

I am looking to get a business card designed for my Building Company. Please find the logo attached.

Industry/Entity Type

Business

Contact Information for Business Card

Mobile 0472 913 046
Email admin@tarrowconstructworks.com.au
Website www.tarrowconstructworks.com.au

Colors
0255a3

```html
<!DOCTYPE html>
<html lang="en">
<head>
<meta charset="utf-8">
<title>Tarrow Construct Works – Business Card</title>
<link href="https://fonts.googleapis.com/css2?family=Montserrat:wght@400;600;700&display=swap" rel="stylesheet">
<style>
  :root {
    --brand-blue: #1e5fad;
    --band-blue-a: #4a78b8;
    --band-blue-b: #3a67a5;
    --band-grey-a: #8a8c8f;
    --band-grey-b: #6d6f72;
    --ink: #3a3a3c;
    --ink-soft: #5a5a5c;
    --paper: #f7f7f5;
    --backdrop: #e9e9e7;
  }
  * { box-sizing: border-box; margin: 0; padding: 0; }
  html, body { width: 1200px; height: 874px; overflow: hidden; }
  body {
    background: var(--backdrop);
    font-family: "Montserrat", sans-serif;
    display: flex;
    flex-direction: column;
    align-items: center;
    justify-content: center;
    gap: 50px;
  }
  .card {
    position: relative;
    width: 560px;
    height: 320px;
    overflow: hidden;
    box-shadow: 0 10px 30px rgba(0,0,0,0.18);
  }
  .corner-band {
    position: absolute;
    left: 0;
    top: 0;
  }

  /* Back */
  .card--back { background: var(--brand-blue); }
  .card--back .corner-band {
    width: 280px;
    height: 120px;
    background: linear-gradient(135deg, var(--band-grey-a), var(--band-grey-b));
  }
  .card--back .wordmark {
    position: absolute;
    left: 200px;
    top: 150px;
    color: #ffffff;
    font-weight: 600;
    font-size: 27px;
    letter-spacing: 0.5px;
  }
  .card--back .web {
    position: absolute;
    right: 32px;
    bottom: 26px;
    color: #ffffff;
    font-size: 13px;
  }

  /* Front */
  .card--front { background: var(--paper); }
  .card--front .corner-band {
    width: 320px;
    height: 62px;
    background: linear-gradient(135deg, var(--band-blue-a), var(--band-blue-b));
  }
  .card--front .wordmark {
    position: absolute;
    right: 30px;
    top: 82px;
    color: var(--brand-blue);
    font-weight: 600;
    font-size: 23px;
    letter-spacing: 0.3px;
  }
  .holder {
    position: absolute;
    left: 72px;
    top: 148px;
  }
  .holder-name {
    color: var(--brand-blue);
    font-weight: 700;
    font-size: 21px;
  }
  .holder-role {
    color: var(--ink-soft);
    font-size: 15px;
    margin-top: 2px;
  }
  .contacts {
    position: absolute;
    left: 72px;
    top: 218px;
    list-style: none;
    font-size: 15px;
    line-height: 27px;
    color: var(--ink);
  }
  .contacts .label {
    display: inline-block;
    width: 26px;
    color: var(--brand-blue);
    font-weight: 600;
  }
</style>
</head>
<body>

  <section class="card card--back" aria-label="Business card back">
    <div class="corner-band" role="img" aria-label="Grey faceted corner decoration"></div>
    <div class="wordmark">Tarrow Construct Works</div>
    <div class="web">tarrowconstructworks.com.au</div>
  </section>

  <section class="card card--front" aria-label="Business card front">
    <div class="corner-band" role="img" aria-label="Blue faceted corner decoration"></div>
    <div class="wordmark">Tarrow Construct Works</div>
    <div class="holder">
      <div class="holder-name">Name, Surname</div>
      <div class="holder-role">position</div>
    </div>
    <ul class="contacts">
      <li><span class="label">M:</span>0472 913 046</li>
      <li><span class="label">E:</span>admin@tarrowconstructworks.com.au</li>
      <li><span class="label">W:</span>www.tarrowconstructworks.com.au</li>
    </ul>
  </section>

</body>
</html>
```